The Book Cover for "Embracing the Quiet Lantern of Dawn" needs redesigned

First the back ground or art work needs to be replaced or redesigned.
The title Embracing the Quiet Lantern of Dawn needs to be redesigned so that the words "Discovering the" is diminished in size compared to the rest of the title "Quiet Lantern of Dawn"
The Sub-title "Tracing the silent journey of the Wandering Flame" needs to be more pronounced and readable.
The authors name needs to be downsized.

```html
<!DOCTYPE html>
<html lang="en">
<head>
<meta charset="utf-8">
<title>Embracing the Quiet Lantern of Dawn — Book Cover</title>
<link href="https://fonts.googleapis.com/css2?family=Marcellus&family=Sorts+Mill+Goudy&family=Cookie&display=swap" rel="stylesheet">
<style>
  :root {
    --backdrop: #e3e3e3;
    --cover-orange: #d95818;
    --cover-orange-deep: #b4441a;
    --title-white: #ffffff;
    --title-navy: #2f4468;
    --band-navy: #3e5a80;
    --tear-white: #ffffff;
    --art-navy: #3c4f86;
    --art-plum: #6a4a6e;
    --art-skin: #e9bfa4;
    --art-amber: #e8822a;
  }
  * { margin: 0; padding: 0; box-sizing: border-box; }
  html, body { width: 1200px; height: 999px; overflow: hidden; background: var(--backdrop); }
  .canvas { position: relative; width: 1200px; height: 999px; }
  .cover {
    position: absolute; left: 267px; top: 0; width: 666px; height: 999px;
    background: linear-gradient(180deg, var(--cover-orange) 0%, var(--cover-orange) 45%, var(--cover-orange-deep) 70%, var(--cover-orange-deep) 78%, var(--cover-orange) 92%);
    overflow: hidden;
  }
  .title-art { position: absolute; left: 0; top: 0; width: 666px; height: 440px; }
  .title-lead { font-family: 'Cookie', cursive; font-size: 50px; fill: var(--title-white); }
  .title-rule { stroke: var(--title-white); stroke-width: 1.5; opacity: .8; }
  .title-main { font-family: 'Marcellus', serif; fill: var(--title-white); }
  .title-accent { font-family: 'Marcellus', serif; fill: var(--title-navy); }
  .art-band { position: absolute; left: 0; top: 436px; width: 666px; height: 310px; }
  .subtitle {
    position: absolute; left: 0; top: 784px; width: 666px; text-align: center;
    font-family: 'Sorts Mill Goudy', serif; font-size: 33px; line-height: 44px;
    color: var(--title-white);
  }
  .author-band {
    position: absolute; left: 0; top: 929px; width: 666px; height: 46px;
    background: var(--band-navy); display: flex; align-items: center; justify-content: center;
  }
  .author-name {
    font-family: 'Sorts Mill Goudy', serif; font-size: 28px; letter-spacing: .5px;
    color: var(--title-white); text-transform: uppercase;
  }
</style>
</head>
<body>
<div class="canvas">
  <section class="cover">
    <svg class="title-art" viewBox="0 0 666 440" aria-label="Embracing the Quiet Lantern of Dawn">
      <line class="title-rule" x1="78" y1="70" x2="195" y2="70"/>
      <line class="title-rule" x1="470" y1="70" x2="580" y2="70"/>
      <text class="title-lead" x="333" y="84" text-anchor="middle">Embracing the</text>
      <text class="title-main" x="345" y="198" text-anchor="middle" font-size="112" textLength="490" lengthAdjust="spacingAndGlyphs">QUIET</text>
      <text class="title-accent" x="345" y="329" text-anchor="middle" font-size="146" textLength="540" lengthAdjust="spacingAndGlyphs">LANTERN</text>
      <text class="title-main" x="345" y="417" text-anchor="middle" font-size="92" textLength="420" lengthAdjust="spacingAndGlyphs">OF DAWN</text>
    </svg>

    <svg class="art-band" viewBox="0 0 666 310" role="img" aria-label="Painted illustration of a mother resting her cheek against a sleeping child among orange flowers">
      <defs>
        <linearGradient id="artFill" x1="0" y1="0" x2="1" y2="0.4">
          <stop offset="0" stop-color="var(--art-navy)"/>
          <stop offset=".45" stop-color="var(--art-plum)"/>
          <stop offset=".7" stop-color="var(--art-skin)"/>
          <stop offset="1" stop-color="var(--art-amber)"/>
        </linearGradient>
      </defs>
      <polygon fill="var(--tear-white)" points="0,36 30,30 55,22 80,28 110,18 140,26 165,20 195,34 230,42 265,38 300,30 330,20 360,8 395,4 420,12 450,14 475,6 505,16 540,12 570,20 600,14 630,22 666,18 666,276 640,274 610,286 580,282 555,294 525,300 495,290 465,276 440,280 410,266 380,258 350,246 320,240 290,248 255,256 225,262 195,270 165,266 135,276 100,270 70,276 40,274 0,280"/>
      <polygon fill="url(#artFill)" points="0,44 30,38 55,30 80,36 110,27 140,34 165,29 195,42 230,50 265,46 300,38 330,28 360,16 395,12 420,20 450,22 475,14 505,24 540,20 570,28 600,22 630,30 666,26 666,266 640,264 610,276 580,272 555,284 525,290 495,280 465,266 440,270 410,256 380,248 350,236 320,230 290,238 255,246 225,252 195,260 165,256 135,266 100,260 70,266 40,264 0,270"/>
    </svg>

    <p class="subtitle">Tracing the silent journey<br>of the Wandering Flame</p>

    <div class="author-band"><span class="author-name">R T Fenwick Halloran</span></div>
  </section>
</div>
</body>
</html>
```